Car Accessory Flyer to advertise parking sensors, heated seats, car security

I'm looking to have a double sided flyer made that will be distributed locally to advertise heated seats and parking sensors on one side. And trackers and Tarvo immobilisers on the other. Our website is www.dernilo.co.uk
I'm hoping its possible to use wording and pictures from our website.

Target Market(s)
Car owners looking to upgrade their car to have parking sensors or heated seats.
Luxury car owners who are worried about their vehicle being stolen.
Industry/Entity Type
Automotive
Requirements
Must have
- Pictures
Our website, phone number and address
Flyer will be A5 double sided
Nice to have
- A design similar to our website

```html
<!DOCTYPE html>
<html lang="en">
<head>
<meta charset="utf-8">
<title>Dernilo – Car Accessories Flyer</title>
<link href="https://fonts.googleapis.com/css2?family=Abel&display=swap" rel="stylesheet">
<style>
  :root {
    --backdrop: #e9e3e6;
    --paper: #f4f3f0;
    --ink: #2c2a28;
    --band: #3a3734;
    --title: #f1efeb;
    --mint: #bfe3d5;
    --footer-text: #d9d6d1;
  }
  * { box-sizing: border-box; margin: 0; padding: 0; }
  html, body { width: 1200px; height: 900px; overflow: hidden; }
  body {
    background: var(--backdrop);
    font-family: "Abel", "Arial Narrow", sans-serif;
    color: var(--ink);
    position: relative;
  }
  .flyer-page {
    position: absolute;
    top: 68px;
    width: 540px;
    height: 764px;
    background: var(--paper);
    overflow: hidden;
    box-shadow: 0 6px 20px rgba(60, 40, 50, 0.18);
  }
  .flyer-page--front { left: 40px; }
  .flyer-page--back { left: 620px; }

  .header-band { position: absolute; top: 0; left: 0; width: 540px; height: 250px; }
  .header-title {
    position: absolute; top: 36px; right: 40px;
    text-align: right; text-transform: uppercase;
    color: var(--title); font-size: 36px; line-height: 1.08; letter-spacing: 0.5px;
    font-weight: 400;
  }

  .service { position: absolute; left: 40px; right: 40px; }
  .service-heading {
    font-size: 28px; font-weight: 400; text-transform: uppercase;
    letter-spacing: 0.5px; line-height: 1;
    padding-bottom: 6px; border-bottom: 1.5px solid var(--ink);
  }
  .service-body { display: flex; justify-content: space-between; margin-top: 10px; }
  .service-text { width: 270px; font-size: 12px; line-height: 1.4; padding-top: 2px; }
  .service-media { width: 170px; text-align: right; flex-shrink: 0; }
  .photo-slot { width: 170px; height: 118px; }
  .price { margin-top: 6px; font-size: 13px; line-height: 1.3; text-align: right; }
  .price-note { font-size: 12px; }

  .photo--car { background: linear-gradient(150deg, #8b8f93 0%, #40464f 55%, #6c6660 100%); }
  .photo--seat-switch { background: radial-gradient(circle at 45% 45%, #8a2a2a 0 8%, #3c3a38 9%, #6b6660 60%, #a39a8f 100%); }
  .photo--map { background: linear-gradient(135deg, #6d7a70 0%, #8d9590 45%, #3b4f85 100%); }
  .photo--immobiliser { background: linear-gradient(140deg, #141619 0%, #2b4a55 55%, #7a2a2a 100%); }

  .address-block {
    position: absolute; right: 40px; top: 540px;
    display: flex; flex-direction: column; align-items: flex-end; gap: 6px;
    font-size: 13px; line-height: 1.2; font-style: normal;
  }
  .address-label { margin-bottom: 4px; }

  .footer-band {
    position: absolute; left: 0; bottom: 0; width: 540px; height: 92px;
    background: var(--band);
    display: flex; align-items: center; justify-content: space-between;
    padding: 0 36px;
  }
  .brand-name { color: var(--mint); font-size: 34px; letter-spacing: 1px; line-height: 1; }
  .contact { text-align: right; color: var(--footer-text); font-size: 14px; line-height: 1.35; }
  .contact-web { text-transform: uppercase; letter-spacing: 0.5px; }
</style>
</head>
<body>

  <section class="flyer-page flyer-page--front">
    <svg class="header-band" viewBox="0 0 540 250" aria-hidden="true">
      <defs>
        <linearGradient id="bandShade" x1="0" y1="0" x2="1" y2="1">
          <stop offset="0" stop-color="#2e2b29"/>
          <stop offset="0.55" stop-color="#4a4541"/>
          <stop offset="1" stop-color="#2f2c2a"/>
        </linearGradient>
      </defs>
      <polygon points="0,0 540,0 540,140 330,192 245,166 0,232" fill="url(#bandShade)"/>
    </svg>
    <h1 class="header-title">Parking Sensors<br>Heated Seats<br>Car Security</h1>

    <article class="service" style="top: 240px;">
      <h2 class="service-heading">Parking Sensors</h2>
      <div class="service-body">
        <p class="service-text">Make parking a breeze by adding parking sensors to your car. We offer a range of different options, our preferred option is flush mount OEM style but have a solution for all vehicles. Our two most poplar options are the standard "mount from the outside" type and the flush OEM style sensors, both can be colour coded.</p>
        <div class="service-media">
          <div class="photo-slot photo--car" role="img" aria-label="Photo of a car in the workshop fitted with rear parking sensors"></div>
          <p class="price">From<br>£190</p>
        </div>
      </div>
    </article>

    <article class="service" style="top: 448px;">
      <h2 class="service-heading">Heated Seats</h2>
      <div class="service-body">
        <p class="service-text">Give yourself the luxury of heated seats. We take your ordinary seats and convert them to heated. From the outside they will look completely standard, we install heating elements to the base and back between the seat cover and foam, with the addition of a conveniently placed switch with the option of High heat, low heat or off. Suitable for both leather and fabric seats.</p>
        <div class="service-media">
          <div class="photo-slot photo--seat-switch" role="img" aria-label="Close-up photo of a heated seat switch beside a car seat"></div>
          <p class="price">£350<br><span class="price-note">for a pair of front seats</span></p>
        </div>
      </div>
    </article>

    <footer class="footer-band">
      <span class="brand-name">DERNILO</span>
      <div class="contact">
        <div class="contact-web">www.dernilo.co.uk</div>
        <div>Call us at 0131 496 0725</div>
      </div>
    </footer>
  </section>

  <section class="flyer-page flyer-page--back">
    <article class="service" style="top: 46px;">
      <h2 class="service-heading">Trackers</h2>
      <div class="service-body">
        <p class="service-text">Keep tabs on your vehicle being moved without you. A discreet GPS tracker is fitted out of sight, letting you follow its location live via a simple app on your phone.</p>
        <div class="service-media">
          <div class="photo-slot photo--map" role="img" aria-label="Screenshot of a tracking app showing a vehicle's location on a satellite map"></div>
          <p class="price"><span class="price-note">From as little as £399 inc the first year subscription then £100 thereafter</span></p>
        </div>
      </div>
    </article>

    <article class="service" style="top: 290px;">
      <h2 class="service-heading">Tarvo</h2>
      <div class="service-body">
        <p class="service-text">The Tarvo immobiliser helps protect your car from key cloning, even if a thief has your keys. You program a personal code using the buttons across your dash or a combination on your steering wheel.</p>
        <div class="service-media">
          <div class="photo-slot photo--immobiliser" role="img" aria-label="Product image of the Tarvo immobiliser with a hand pressing security icons"></div>
          <p class="price">From<br>£449</p>
        </div>
      </div>
    </article>

    <address class="address-block">
      <span class="address-label">Address</span>
      <span>14 Harrowfield Yards</span>
      <span>Edinburgh</span>
      <span>EH7 2QX</span>
    </address>

    <footer class="footer-band">
      <span class="brand-name">DERNILO</span>
      <div class="contact">
        <div class="contact-web">www.dernilo.co.uk</div>
        <div>Call us at 0131 496 0725</div>
      </div>
    </footer>
  </section>

</body>
</html>
```